Business Card Design for www.valtrenco.eu

- Our business: we help European companies source, outsource and invest in Asia
- Target market: companies in European Union (France, Belgium, Germany...)
- Business based in Luxembourg with operations in Singapore, India, Vietnam...

```html
<!DOCTYPE html>
<html lang="en">
<head>
<meta charset="utf-8">
<title>Valtrenco Business Card</title>
<link rel="stylesheet" href="https://fonts.googleapis.com/css2?family=Arimo:ital,wght@0,400;0,700;1,400&display=swap">
<style>
  :root {
    --maroon: #6a0a0a;
    --tan: #d9a27c;
    --white: #ffffff;
    --backdrop: #e9e6e2;
    --ink: #6a0a0a;
  }
  * { margin: 0; padding: 0; box-sizing: border-box; }
  html, body {
    width: 1200px; height: 560px; overflow: hidden;
    background: var(--backdrop);
    font-family: "Arimo", Arial, sans-serif;
  }
  .canvas { position: relative; width: 1200px; height: 560px; }
  .card {
    position: absolute; top: 132px;
    width: 540px; height: 296px;
    box-shadow: 0 2px 8px rgba(0,0,0,0.18);
  }
  .card-front { left: 56px; background: var(--maroon); }
  .card-back { left: 604px; background: var(--white); overflow: hidden; }

  .brand {
    position: absolute; left: 0; right: 0; top: 100px;
    text-align: center;
  }
  .brand-name {
    display: inline-block;
    color: var(--tan);
    font-size: 42px; font-weight: 400;
    letter-spacing: 11px; line-height: 1;
    padding-left: 11px;
  }
  .brand-rule {
    width: 342px; height: 1px; margin: 10px auto 6px;
    background: var(--tan);
  }
  .tagline {
    color: var(--white); font-size: 14.5px; letter-spacing: 0.2px;
  }
  .cities {
    position: absolute; left: 26px; right: 20px; bottom: 26px;
    display: flex; gap: 10px;
    color: var(--white); font-size: 13px;
    list-style: none;
  }
  .cities li::before { content: "\2726"; margin-right: 4px; font-size: 11px; }

  .arrow-panel { position: absolute; left: 0; top: 0; }
  .mini-brand {
    position: absolute; left: 10px; top: 128px; width: 140px;
  }
  .mini-brand-name {
    color: var(--tan); font-size: 20px; letter-spacing: 3px; line-height: 1;
  }
  .mini-tagline {
    color: var(--white); font-size: 5.6px; margin-top: 4px; white-space: nowrap;
  }
  .contact {
    position: absolute; left: 204px; top: 22px;
    color: var(--ink);
  }
  .contact-name { font-size: 18.5px; font-weight: 700; letter-spacing: 0.6px; }
  .contact-role { font-size: 13.5px; font-style: italic; letter-spacing: 0.4px; margin-top: 1px; }
  .contact-block { font-size: 17px; line-height: 22px; letter-spacing: 0.3px; margin-top: 14px; }
</style>
</head>
<body>
<main class="canvas">
  <section class="card card-front">
    <div class="brand">
      <div class="brand-name">VALTRENCO</div>
      <div class="brand-rule"></div>
      <div class="tagline">DEVELOPMENT YOUR BUSINESS WITH ASIA</div>
    </div>
    <ul class="cities">
      <li>Bangkok</li><li>Beijing</li><li>Jakarta</li><li>Kochi</li><li>Saigon</li><li>Shanghai</li><li>Singapore</li>
    </ul>
  </section>

  <section class="card card-back">
    <svg class="arrow-panel" width="540" height="296" viewBox="0 0 540 296" aria-hidden="true">
      <polygon points="0,0 194,148 0,296" fill="var(--maroon)"/>
    </svg>
    <div class="mini-brand">
      <div class="mini-brand-name">VALTRENCO</div>
      <div class="mini-tagline">DEVELOPMENT YOUR BUSINESS WITH ASIA</div>
    </div>
    <div class="contact">
      <div class="contact-name">Mathis Verhaegen</div>
      <div class="contact-role">Co-Founder</div>
      <div class="contact-block">
        Lindenhof Office Centre<br>
        7-9 rue Albert Kessler<br>
        L-2318 Luxembourg
      </div>
      <div class="contact-block">
        P: (352) 20 55 71 8820<br>
        F: (352) 41 73 09 2264
      </div>
      <div class="contact-block">
        mathis.verhaegen@valtrenco.eu<br>
        www.valtrenco.eu
      </div>
    </div>
  </section>
</main>
</body>
</html>
```